Online Greeting Card Marketplace redesign

PennedNotes.com is a two-sided greeting card marketplace. Buyers purchase hand-made cards online, indicating their message. Sellers hand-write the message and mail directly to recipient.

We are getting decent foot traffic but low sales. I'm also not drawing a lot of Card Designers to sell their products. Feedback has been that it's cluttered, boring, and out of date.

I've always enjoyed vibes such as Lana Brookfield and Delia Hartwell. I was going for pale blues and chocolate browns (as can be seen in PennedNotes Friendbook and Chirpline pages).

Attached document is my not-so-great attempt to redesign, which is uninviting and unpolished.

Need a new homepage and a second similar page when shopping (click on any category to see what I mean, e.g. Halloween).
Updates

Industry/Entity Type

Shopping

Requirements
Must have
• I think my logo (stick drawing of a man with an envelope) is what is currently driving a lot of traffic and should stay in the design, pending minor tweaks.

I'll need all the details of the final design to give to the programmers (font styles, color numbers, etc).

Nice to have
• I was thinking of a dotted frame to surround each picture? White Pearl luminescent or a metallic? I just don't know if it works.

```html
<!DOCTYPE html>
<html lang="en">
<head>
<meta charset="utf-8">
<title>Create Account – PennedNotes.com</title>
<link href="https://fonts.googleapis.com/css2?family=Lato:wght@400;700;900&family=Pacifico&display=swap" rel="stylesheet">
<style>
  :root {
    --teal: #5fbac9;
    --teal-dark: #2f8d9c;
    --sky: #d1eef4;
    --page: #f8f8f8;
    --cocoa: #3a2c2a;
    --ink: #333333;
    --link-yellow: #f6e85c;
    --nav-red: #f0626a;
    --nav-teal: #56b9c9;
    --nav-violet: #6d6db3;
    --nav-orange: #f5891f;
    --badge: #f04e6a;
    --field-border: #a9a9a9;
    --white: #ffffff;
  }
  * { box-sizing: border-box; margin: 0; padding: 0; }
  html, body { width: 1200px; height: 842px; overflow: hidden; }
  body {
    position: relative;
    background: var(--page);
    font-family: "Lato", Arial, sans-serif;
    color: var(--ink);
  }

  /* Top utility bar */
  .utility-bar {
    position: absolute; left: 0; top: 0; width: 1200px; height: 52px;
    background: var(--teal);
  }
  .welcome {
    position: absolute; left: 158px; top: 17px;
    font-size: 11.7px; color: var(--white);
  }
  .welcome a { color: var(--link-yellow); text-decoration: none; }
  .search {
    position: absolute; left: 550px; top: 12px; width: 314px; height: 24px;
    background: #effbfc; border-radius: 3px;
  }
  .search-label {
    position: absolute; left: 11px; top: 6px;
    font-size: 10px; letter-spacing: 0.5px; color: #6b8f96;
  }
  .search svg { position: absolute; right: 6px; top: 4px; }
  .cart-icon { position: absolute; left: 957px; top: 11px; }
  .cart-label {
    position: absolute; left: 1003px; top: 6px;
    font-size: 10px; font-weight: 900; color: var(--white);
  }
  .cart-count {
    position: absolute; left: 1000px; top: 21px; width: 33px; height: 16px;
    background: var(--badge); border-radius: 2px;
    font-size: 10px; font-weight: 900; color: var(--white);
    text-align: center; line-height: 16px;
  }

  /* Masthead */
  .masthead {
    position: absolute; left: 0; top: 52px; width: 1200px; height: 118px;
    background: var(--sky);
  }
  .brand {
    position: absolute; left: 160px; top: 92px;
    display: flex; align-items: center; gap: 12px;
  }
  .brand-dot { width: 34px; height: 34px; border-radius: 50%; background: var(--teal); }
  .brand-name { font-size: 32px; font-weight: 700; color: var(--cocoa); }
  .main-nav {
    position: absolute; left: 590px; top: 105px;
    display: flex; gap: 20px;
    font-size: 11.8px; font-weight: 700; text-transform: uppercase;
  }
  .main-nav a { text-decoration: none; }
  .nav-holidays { color: var(--nav-red); }
  .nav-everyday { color: var(--nav-teal); }
  .nav-birthdays { color: var(--nav-violet); }
  .nav-all { color: var(--nav-orange); }

  /* Page content */
  .page-title {
    position: absolute; left: 157px; top: 196px;
    font-family: "Pacifico", cursive; font-weight: 400;
    font-size: 44px; color: var(--cocoa); line-height: 1.4;
  }
  .role-option {
    position: absolute;
    display: flex; align-items: center; gap: 16px;
  }
  .role-designer { left: 167px; top: 288px; }
  .role-customer { left: 548px; top: 285px; }
  .checkbox {
    width: 23px; height: 23px; background: var(--white);
    border: 1px solid #9a9a9a; border-radius: 3px;
  }
  .role-title { font-size: 20.5px; color: var(--ink); }
  .role-note { font-size: 12.5px; color: var(--ink); margin-left: 4px; }
  .role-customer .role-note { margin-left: 10px; }

  .signup-form {
    position: absolute; left: 160px; top: 344px; width: 908px; height: 333px;
    border: 2px dotted #3a3a3a;
  }
  .field-label {
    position: absolute; left: 38px; font-size: 20px; color: var(--ink);
  }
  .label-email { top: 33px; }
  .label-password { top: 144px; }
  .text-field {
    position: absolute; left: 35px; width: 834px; height: 50px;
    background: var(--white); border: 1px solid var(--field-border); border-radius: 4px;
  }
  .field-email { top: 67px; }
  .field-password { top: 178px; }
  .submit-button {
    position: absolute; left: 759px; top: 256px; width: 115px; height: 46px;
    background: var(--teal); border: none; border-bottom: 3px solid var(--teal-dark);
    border-radius: 3px;
    font-family: "Lato", Arial, sans-serif; font-size: 18px; font-weight: 900;
    color: var(--white);
  }

  /* Footer */
  .site-footer {
    position: absolute; left: 0; top: 768px; width: 1200px; height: 74px;
    background: var(--teal);
  }
  .copyright {
    position: absolute; left: 158px; top: 33px; font-size: 10px; color: var(--white);
  }
  .footer-link {
    position: absolute; top: 32px;
    font-size: 11px; color: var(--white); text-decoration: none;
  }
  .link-about { left: 768px; }
  .link-contact { left: 857px; }
  .link-follow { left: 918px; }
  .link-chirpline { left: 970px; }
  .link-friendbook { left: 1022px; }
</style>
</head>
<body>

<header class="utility-bar">
  <p class="welcome">Welcome Visitor you can <a href="#">Sign In</a> or <a href="#">create an account</a></p>
  <div class="search">
    <span class="search-label">SEARCH</span>
    <svg width="16" height="16" viewBox="0 0 16 16" aria-hidden="true">
      <circle cx="9.5" cy="6.5" r="4.5" fill="none" stroke="#6fb8a8" stroke-width="1.6"/>
      <line x1="6.3" y1="9.7" x2="2.5" y2="13.5" stroke="#6fb8a8" stroke-width="2" stroke-linecap="round"/>
    </svg>
  </div>
  <svg class="cart-icon" width="28" height="24" viewBox="0 0 28 24" aria-hidden="true">
    <path d="M8 9 L14 2 L20 9" fill="none" stroke="#fff" stroke-width="2.4" stroke-linejoin="round"/>
    <path d="M1 9 H27 L24 23 H4 Z" fill="#fff"/>
    <rect x="9" y="13" width="10" height="5" rx="1" fill="#5fbac9"/>
  </svg>
  <span class="cart-label">CART</span>
  <span class="cart-count">2</span>
</header>

<div class="masthead"></div>
<div class="brand">
  <span class="brand-dot"></span>
  <span class="brand-name">pennednotes.com</span>
</div>
<nav class="main-nav">
  <a class="nav-holidays" href="#">Upcoming Holidays</a>
  <a class="nav-everyday" href="#">Every Day Cards</a>
  <a class="nav-birthdays" href="#">Birthdays</a>
  <a class="nav-all" href="#">All Categories</a>
</nav>

<main>
  <h1 class="page-title">Create Account</h1>

  <label class="role-option role-designer">
    <span class="checkbox"></span>
    <span><span class="role-title">I am a Designer</span><span class="role-note">I want to submit designs</span></span>
  </label>
  <label class="role-option role-customer">
    <span class="checkbox"></span>
    <span><span class="role-title">I am a Customer</span><span class="role-note">I want to purchase cards</span></span>
  </label>

  <form class="signup-form">
    <span class="field-label label-email">Your Email</span>
    <div class="text-field field-email"></div>
    <span class="field-label label-password">Your Password</span>
    <div class="text-field field-password"></div>
    <button class="submit-button" type="button">Submit</button>
  </form>
</main>

<footer class="site-footer">
  <p class="copyright">All rights reserved © 2011-2013 Penned Notes</p>
  <a class="footer-link link-about" href="#">About Us/FAQ</a>
  <a class="footer-link link-contact" href="#">Contact</a>
  <span class="footer-link link-follow">Follow Us</span>
  <a class="footer-link link-chirpline" href="#">Chirpline</a>
  <a class="footer-link link-friendbook" href="#">Friendbook</a>
</footer>

</body>
</html>
```